Business Landing Page for SEO Company

Need the landing page of the website designed - I will provide the copy, will need to include details of my company and the services offered, about us, testimonials, faq, etc., and all these elements will need to be arranged graphically on the page.

I want something similar to this: https://pebrovault.com/

Not in terms of color or theme or anything, but we offer a similar service and want to display similar information.

Th services we provide are:

Premium Links
Monthly Links Subscription
Link Insertions

Need to advertise them on the front page. Additionally need a place for testimonials, company details, etc.,

We already have logo for the website. Please use the attached file to insert the logo within the overal design.

Target Market(s)

SEO marketers and agencies

Number of Pages Required

1 page

```html
<!DOCTYPE html>
<html lang="en">
<head>
<meta charset="utf-8">
<title>Linkora – Done-For-You Link Building</title>
<link href="https://fonts.googleapis.com/css2?family=Montserrat:wght@400;500;600;700;800&family=Open+Sans:wght@400;600&display=swap" rel="stylesheet">
<style>
:root{
  --blue:#1565d8;
  --blue-deep:#0d4fb8;
  --blue-light:#3f8cf0;
  --orange:#f68b1f;
  --ink:#1d2a3a;
  --muted:#6b7684;
  --pale:#eef1f6;
  --white:#ffffff;
  --line:#9fc0ea;
}
*{box-sizing:border-box;margin:0;padding:0}
html,body{width:1200px;height:3572px;overflow:hidden}
body{font-family:"Open Sans",Arial,sans-serif;color:var(--ink);background:var(--white);position:relative}
h1,h2,h3,.nav,.btn,.wordmark{font-family:"Montserrat",Arial,sans-serif}
section,header,footer{position:absolute;left:0;width:1200px}

/* header */
.site-header{top:0;height:110px;background:var(--white);display:flex;align-items:center;padding:0 96px}
.wordmark{font-weight:700;font-size:40px;color:var(--ink);letter-spacing:0}
.nav{margin-left:auto;display:flex;align-items:center;gap:34px;font-size:15px;font-weight:700;color:var(--ink)}
.nav .login{background:var(--orange);color:var(--white);border-radius:20px;padding:7px 26px;font-size:13px}
.nav svg{width:16px;height:16px}

/* hero */
.hero{top:110px;height:570px;background:linear-gradient(180deg,var(--blue) 0%,var(--blue-deep) 100%);overflow:hidden}
.hero-copy{position:absolute;left:96px;top:156px;width:480px;color:var(--white)}
.hero-copy h1{font-size:31px;font-weight:800;line-height:1.22;text-transform:uppercase}
.hero-copy p{font-size:13px;line-height:1.6;margin-top:16px;opacity:.92}
.btn{display:inline-flex;align-items:center;gap:10px;background:var(--orange);color:var(--white);font-size:11px;font-weight:700;border-radius:4px;padding:10px 16px;text-transform:uppercase;margin-top:26px}
.btn .arr{width:18px;height:18px;border:2px solid var(--white);border-radius:50%;display:inline-block;position:relative}
.btn .arr::after{content:"";position:absolute;left:3px;top:4px;width:5px;height:5px;border-top:2px solid var(--white);border-right:2px solid var(--white);transform:rotate(45deg)}
.hero-art{position:absolute;left:620px;top:10px;width:540px;height:530px;border-radius:48% 52% 40% 60% / 55% 45% 55% 45%;background:radial-gradient(circle at 50% 45%,#dfe9fb 0%,#a9c7f3 45%,#7d52d9 100%);opacity:.95}

/* services */
.services{top:680px;height:520px;text-align:center}
.eyebrow{font-family:"Montserrat",Arial,sans-serif;font-size:12px;font-weight:700;color:var(--orange);letter-spacing:1px;text-transform:uppercase}
.section-title{font-size:50px;font-weight:800;color:var(--blue);text-transform:uppercase;letter-spacing:1px}
.services .eyebrow{margin-top:38px}
.services .section-title{margin-top:2px}
.service-row{position:absolute;top:170px;left:80px;width:1040px;height:320px}
.service{position:absolute;width:300px;height:280px;display:flex;flex-direction:column;align-items:center;justify-content:center;padding:0 40px}
.service.left{left:0;top:20px;background:#f4f4f6;border-radius:46% 54% 50% 50% / 58% 52% 48% 42%;box-shadow:0 10px 30px rgba(0,0,0,.08)}
.service.center{left:350px;top:-20px;width:340px;height:330px;background:linear-gradient(160deg,var(--blue-light),var(--blue-deep));border-radius:40% 60% 55% 45% / 45% 40% 60% 55%;color:var(--white)}
.service.right{left:740px;top:20px;background:#f4f4f6;border-radius:54% 46% 50% 50% / 50% 58% 42% 50%;box-shadow:0 10px 30px rgba(0,0,0,.08)}
.service svg{width:44px;height:44px;margin-bottom:12px}
.service h3{font-size:19px;font-weight:700;color:var(--blue);margin-bottom:10px}
.service.center h3{color:var(--white)}
.service p{font-size:11px;line-height:1.55;color:var(--muted)}
.service.center p{color:#dce9fc}
.service .more{font-family:"Montserrat",Arial,sans-serif;font-size:11px;font-weight:700;color:var(--orange);margin-top:14px}
.service.center .more{color:var(--white)}

.faint-name{position:absolute;top:1190px;left:60px;font-family:"Montserrat",Arial,sans-serif;font-weight:700;font-size:190px;color:#f1f2f5;line-height:1}

/* about */
.about{top:1380px;height:360px;background:var(--pale)}
.about-art{position:absolute;left:150px;top:36px;width:460px;height:290px;border-radius:12px;background:linear-gradient(135deg,#dbe7f8,#b9d0f2)}
.about-copy{position:absolute;left:640px;top:60px;width:440px}
.about-copy h2{font-size:40px;font-weight:800;color:var(--blue);text-transform:uppercase;line-height:1.05;margin-top:4px}
.about-copy p{font-size:13px;line-height:1.6;color:var(--ink);margin-top:12px}

/* testimonials */
.testimonials{top:1740px;height:670px;background:linear-gradient(180deg,var(--blue) 0%,var(--blue-deep) 100%);text-align:center}
.testimonials .section-title{color:var(--white);margin-top:170px}
.quotes{position:absolute;top:280px;left:100px;width:1000px;display:flex;gap:40px}
.quote{width:306px}
.quote .card{background:var(--white);height:190px;padding:34px 30px;font-size:12px;line-height:1.65;color:var(--muted);text-align:left;box-shadow:0 8px 20px rgba(0,0,0,.15)}
.person{display:flex;align-items:center;gap:14px;margin-top:-10px;padding-left:10px}
.avatar{width:58px;height:58px;border-radius:50%;background:#c9a07c;border:3px solid var(--white)}
.person .name{font-family:"Montserrat",Arial,sans-serif;font-size:13px;font-weight:700;color:var(--orange);text-transform:uppercase;text-align:left;margin-top:16px}
.person .role{font-size:11px;color:var(--white);text-align:left}
.dots{position:absolute;top:560px;left:0;width:1200px;display:flex;justify-content:center;gap:6px}
.dots span{width:18px;height:5px;background:#8ab3ef;border-radius:3px}
.dots span.on{background:var(--orange)}

/* faq */
.faq{top:2410px;height:400px}
.faq h2{position:absolute;left:96px;top:38px;font-size:40px;font-weight:800;color:var(--blue);text-transform:uppercase;line-height:1.1}
.faq-list{position:absolute;left:96px;top:150px;width:406px}
.faq-item{display:flex;justify-content:space-between;align-items:center;border:1.5px solid var(--orange);height:46px;padding:0 14px;margin-bottom:14px;font-size:12px;font-weight:600}
.faq-item svg{width:16px;height:16px;flex:none}
.faq-art{position:absolute;left:560px;top:20px;width:540px;height:370px;border-radius:50% 50% 44% 56% / 48% 52% 48% 52%;background:radial-gradient(circle at 50% 50%,#fdf0c8 0%,#eef3fb 55%,#ffffff 80%)}

/* contact */
.contact{top:2790px;height:440px;text-align:center}
.fields{position:absolute;left:96px;top:110px;width:1008px;display:flex;gap:18px}
.field{flex:1;height:56px;border:1.5px solid var(--line);text-align:left;padding:12px;font-size:11px;color:#9aa4b1}
.textarea{position:absolute;left:96px;top:184px;width:1008px;height:170px;border:1.5px solid var(--line);text-align:left;padding:12px;font-size:11px;color:#9aa4b1}
.send{position:absolute;left:96px;top:370px;width:1008px;height:50px;background:var(--blue);color:var(--white);font-family:"Montserrat",Arial,sans-serif;font-weight:600;font-size:16px;display:flex;align-items:center;justify-content:center;text-transform:uppercase}

/* footer */
.site-footer{top:3240px;height:292px}
.footer-map{position:absolute;left:120px;top:10px;width:960px;height:270px;background:radial-gradient(ellipse at center,#e9edf3 0%,#ffffff 70%)}
.site-footer .wordmark{position:absolute;left:0;width:1200px;text-align:center;top:22px;font-size:56px}
.contact-row{position:absolute;top:128px;left:310px;width:580px;display:flex;justify-content:space-between}
.contact-item{width:180px;text-align:center;font-size:13px;color:var(--ink)}
.contact-item .ic{width:44px;height:44px;border-radius:50%;background:var(--orange);margin:0 auto 14px;display:flex;align-items:center;justify-content:center}
.contact-item .ic svg{width:20px;height:20px}
.socials{position:absolute;right:96px;top:190px;display:flex;gap:8px}
.socials span{width:24px;height:24px;border-radius:50%;background:var(--orange)}
.copyright{position:absolute;top:3532px;left:0;width:1200px;height:40px;background:var(--blue);color:var(--white);font-size:11px;display:flex;align-items:center;padding-left:96px}
</style>
</head>
<body>

<header class="site-header">
  <div class="wordmark">Linkora</div>
  <nav class="nav">
    <span>Home</span><span>Services Offered</span><span>About Us</span><span>Testimonials</span><span>Faq</span>
    <span class="login">Log In</span>
    <svg viewBox="0 0 16 16" fill="none" stroke="#1565d8" stroke-width="2"><circle cx="7" cy="7" r="5"/><line x1="11" y1="11" x2="15" y2="15"/></svg>
  </nav>
</header>

<section class="hero">
  <div class="hero-copy">
    <h1>The Real Done-For-You Link Building Service</h1>
    <p>Lorem Ipsum is simply dummy text of the printing and typesetting industry. Lorem Ipsum has been the industry's standard dummy text ever since the 1500s, when an unknown printer took a galley of type and scrambled it to make a type specimen book.</p>
    <span class="btn">Learn More <span class="arr"></span></span>
  </div>
  <div class="hero-art" role="img" aria-label="Illustration of a person studying a large web analytics dashboard among stylised plants"></div>
</section>

<section class="services">
  <div class="eyebrow">What We Offer</div>
  <h2 class="section-title">Services Offered</h2>
  <div class="service-row">
    <div class="service left">
      <svg viewBox="0 0 44 44" fill="none" stroke="#f68b1f" stroke-width="2.5"><polygon points="22,5 27,17 40,18 30,27 33,40 22,33 11,40 14,27 4,18 17,17"/></svg>
      <h3>Premium Links</h3>
      <p>Lorem Ipsum is simply dummy text of the printing and typesetting industry. Lorem Ipsum has been the industry's.</p>
      <div class="more">READ MORE</div>
    </div>
    <div class="service center">
      <svg viewBox="0 0 44 44" fill="none" stroke="#ffffff" stroke-width="2.5"><rect x="6" y="9" width="32" height="28" rx="3"/><line x1="6" y1="17" x2="38" y2="17"/><line x1="14" y1="5" x2="14" y2="12"/><line x1="30" y1="5" x2="30" y2="12"/></svg>
      <h3>Monthly Links Subscription</h3>
      <p>Lorem Ipsum is simply dummy text of the printing and typesetting industry. Lorem Ipsum has been the industry's.</p>
      <div class="more">READ MORE</div>
    </div>
    <div class="service right">
      <svg viewBox="0 0 44 44" fill="none" stroke="#f68b1f" stroke-width="3" stroke-linecap="round"><path d="M19 25a7 7 0 0 0 10 0l6-6a7 7 0 0 0-10-10l-3 3"/><path d="M25 19a7 7 0 0 0-10 0l-6 6a7 7 0 0 0 10 10l3-3"/></svg>
      <h3>Link Insertions</h3>
      <p>Lorem Ipsum is simply dummy text of the printing and typesetting industry. Lorem Ipsum has been the industry's.</p>
      <div class="more">READ MORE</div>
    </div>
  </div>
</section>

<div class="faint-name" aria-hidden="true">Linkora</div>

<section class="about">
  <div class="about-art" role="img" aria-label="Line illustration of a laptop on a desk with a lamp, plant and coffee cup"></div>
  <div class="about-copy">
    <div class="eyebrow">Welcome Our Company</div>
    <h2>About Our Company</h2>
    <p>Lorem Ipsum is simply dummy text of the printing and typesetting industry. Lorem Ipsum has been the industry's standard dummy text ever since the 1500s, when an unknown printer took a galley of type and scrambled it to make a type specimen book. Lorem Ipsum is simply dummy text of the printing and typesetting industry. Lorem Ipsum has been the industry's standard dummy text ever since the 1500s.</p>
    <span class="btn">Learn More <span class="arr"></span></span>
  </div>
</section>

<section class="testimonials">
  <h2 class="section-title">Testimonials</h2>
  <div class="quotes">
    <div class="quote">
      <div class="card">Enim maxime tempora incidunt laboriosam ciditis, aut cum accidunt sint, ad quam soluta voluptate nobis quibusdam aut maxime consequuntur rerum ut, voluptas nulla quas sit magni dolor adipiscing elit, sed do eiusmod.</div>
      <div class="person"><div class="avatar" role="img" aria-label="Client portrait"></div><div><div class="name">Daniel Reyes</div><div class="role">Project Manager</div></div></div>
    </div>
    <div class="quote">
      <div class="card">Enim maxime tempora incidunt laboriosam ciditis, aut cum accidunt sint, ad quam soluta voluptate nobis quibusdam aut maxime consequuntur rerum ut, voluptas nulla quas sit magni dolor adipiscing elit, sed do eiusmod.</div>
      <div class="person"><div class="avatar" role="img" aria-label="Client portrait"></div><div><div class="name">Daniel Reyes</div><div class="role">Project Manager</div></div></div>
    </div>
    <div class="quote">
      <div class="card">Enim maxime tempora incidunt laboriosam ciditis, aut cum accidunt sint, ad quam soluta voluptate nobis quibusdam aut maxime consequuntur rerum ut, voluptas nulla quas sit magni dolor adipiscing elit, sed do eiusmod.</div>
      <div class="person"><div class="avatar" role="img" aria-label="Client portrait"></div><div><div class="name">Daniel Reyes</div><div class="role">Project Manager</div></div></div>
    </div>
  </div>
  <div class="dots"><span class="on"></span><span></span><span></span></div>
</section>

<section class="faq">
  <h2>Frequently<br>Ask Question</h2>
  <div class="faq-list">
    <div class="faq-item">Lorem Ipsum is simply dummy text of the printing<svg viewBox="0 0 16 16" fill="none" stroke="#f68b1f" stroke-width="1.6"><circle cx="8" cy="8" r="7"/><line x1="8" y1="4.5" x2="8" y2="11.5"/><line x1="4.5" y1="8" x2="11.5" y2="8"/></svg></div>
    <div class="faq-item">Lorem Ipsum is simply dummy text of the printing<svg viewBox="0 0 16 16" fill="none" stroke="#f68b1f" stroke-width="1.6"><circle cx="8" cy="8" r="7"/><line x1="8" y1="4.5" x2="8" y2="11.5"/><line x1="4.5" y1="8" x2="11.5" y2="8"/></svg></div>
    <div class="faq-item">Lorem Ipsum is simply dummy text of the printing<svg viewBox="0 0 16 16" fill="none" stroke="#f68b1f" stroke-width="1.6"><circle cx="8" cy="8" r="7"/><line x1="8" y1="4.5" x2="8" y2="11.5"/><line x1="4.5" y1="8" x2="11.5" y2="8"/></svg></div>
  </div>
  <div class="faq-art" role="img" aria-label="Illustration of a group of people standing beside large yellow question and exclamation marks"></div>
</section>

<section class="contact">
  <h2 class="section-title">Contact Us</h2>
  <div class="fields">
    <div class="field">Your Name*</div>
    <div class="field">Your Phone*</div>
    <div class="field">Your E-mail address*</div>
  </div>
  <div class="textarea">Your Message</div>
  <div class="send">Send Message</div>
</section>

<footer class="site-footer">
  <div class="footer-map" role="img" aria-label="Faint dotted world map backdrop"></div>
  <div class="wordmark">Linkora</div>
  <div class="contact-row">
    <div class="contact-item">
      <div class="ic"><svg viewBox="0 0 20 20" fill="#fff"><path d="M10 1a6 6 0 0 0-6 6c0 4.5 6 12 6 12s6-7.5 6-12a6 6 0 0 0-6-6zm0 8.3a2.3 2.3 0 1 1 0-4.6 2.3 2.3 0 0 1 0 4.6z"/></svg></div>
      Harbor City, Northland
    </div>
    <div class="contact-item">
      <div class="ic"><svg viewBox="0 0 20 20" fill="#fff"><path d="M5 2l3 4-2 2c1 2 3 4 6 6l2-2 4 3-2 3C9 18 2 11 2 4z"/></svg></div>
      0100-555-0142
    </div>
    <div class="contact-item">
      <div class="ic"><svg viewBox="0 0 20 20" fill="none" stroke="#fff" stroke-width="1.8"><rect x="2" y="4" width="16" height="12" rx="1"/><polyline points="2,5 10,11 18,5"/></svg></div>
      hello@linkora-mail.com
    </div>
  </div>
  <div class="socials" aria-label="Social links"><span></span><span></span><span></span><span></span></div>
</footer>

<div class="copyright">COPYRIGHT © 2021 LINKORA. ALL RIGHTS RESERVED</div>

</body>
</html>
```